Electrician Business Card/ company logo/small business

New Business Cards and logo needed that will catch peoples eye and say we went that extra step. Attached is a design possibly to be incorporated, if u have your own great, lets see it!... This will be a small local business. thank you for all you do!
Corvane Electric
Wren Osloby Owner
Journeyman Electrician
phone 1.360.428.6037
email: KLXCorvaneElectric@mailvex.net
call for free estimate!

Target Market(s)

support small local business

Industry/Entity Type

Electrical,

Contact Information for Business Card

name, title,company/ logo, phone, email, free estimate

Font styles to use
Other font styles liked:
• easy to read

Colors

Designer to choose colors to be used in the design.

Requirements
Must have
• eye catching everything! logo and corvane electric listed on business card/logo, incorp logo in the background of card
Nice to have
• lightening bolts in eyes or around the triangle? vertical, modern, any design that would be unique and stand out
Should not have
• pinks, reds, yellows,brown

```html
<!DOCTYPE html>
<html lang="en">
<head>
<meta charset="utf-8">
<title>Corvane Electric – Business Card</title>
<link rel="stylesheet" href="https://fonts.googleapis.com/css2?family=Lato:wght@400&family=Orbitron:wght@700&display=swap">
<style>
  :root {
    --backdrop: #4b4b4b;
    --card-white: #ffffff;
    --card-black: #000000;
    --ink: #111111;
    --brand-blue: #1a8fd8;
    --band-start: #00aeef;
    --band-mid: #0a7fc6;
    --band-end: #2e3192;
  }
  html, body {
    margin: 0;
    padding: 0;
    width: 1200px;
    height: 960px;
    overflow: hidden;
    background: var(--backdrop);
  }
  .canvas {
    position: relative;
    width: 1200px;
    height: 960px;
  }
  .card {
    position: absolute;
    width: 761px;
    height: 435px;
    overflow: hidden;
  }
  .card-front {
    left: 129px;
    top: 40px;
    background: var(--card-white);
  }
  .card-back {
    left: 263px;
    top: 496px;
    background: var(--card-black);
  }
  .brand-name {
    position: absolute;
    margin: 0;
    font-family: "Orbitron", sans-serif;
    font-weight: 700;
    color: var(--brand-blue);
    text-align: center;
    text-transform: uppercase;
    line-height: 1.15;
  }
  .card-front .brand-name {
    left: 29px;
    width: 300px;
    top: 168px;
    font-size: 34px;
  }
  .card-back .brand-name {
    left: 0;
    width: 761px;
    top: 165px;
    font-size: 44px;
  }
  .divider {
    position: absolute;
    left: 345px;
    top: 94px;
    width: 2px;
    height: 248px;
    background: var(--ink);
  }
  .contact {
    position: absolute;
    left: 373px;
    top: 168px;
    color: var(--ink);
    font-family: "Lato", sans-serif;
  }
  .person-name {
    margin: 0;
    font-family: "Orbitron", sans-serif;
    font-weight: 700;
    font-size: 29px;
    letter-spacing: 1px;
    text-transform: uppercase;
    line-height: 1;
  }
  .person-title {
    margin: 6px 0 0;
    font-size: 22px;
    line-height: 1.2;
  }
  .contact-list {
    list-style: none;
    margin: 18px 0 0;
    padding: 0;
    font-size: 21px;
    line-height: 29px;
  }
  .contact-list li {
    display: flex;
    align-items: center;
  }
  .contact-icon {
    width: 17px;
    height: 17px;
    margin-right: 12px;
    flex: none;
  }
  .accent-band {
    position: absolute;
    left: 0;
    bottom: 0;
    width: 100%;
    height: 25px;
    background: linear-gradient(90deg, var(--band-start), var(--band-mid) 50%, var(--band-end));
  }
</style>
</head>
<body>
<main class="canvas">
  <section class="card card-front">
    <p class="brand-name">Corvane<br>Electric</p>
    <div class="divider"></div>
    <div class="contact">
      <h1 class="person-name">Wren Osloby</h1>
      <p class="person-title">Journeyman Electrician</p>
      <ul class="contact-list">
        <li>
          <svg class="contact-icon" viewBox="0 0 17 17" aria-hidden="true">
            <rect width="17" height="17" rx="3" fill="#1a8fd8"/>
            <path d="M5 4 L7 4 L8 6.5 L6.8 7.5 Q7.8 9.5 9.5 10.2 L10.5 9 L13 10 L13 12 Q12 13.5 10 13 Q5.5 11.5 4 7 Q3.7 5 5 4 Z" fill="#ffffff"/>
          </svg>
          1.360.428.6037
        </li>
        <li>
          <svg class="contact-icon" viewBox="0 0 17 17" aria-hidden="true">
            <path d="M1 7 L8.5 2 L16 7 L16 15 L1 15 Z" fill="#1a8fd8"/>
            <path d="M1 7 L8.5 11.5 L16 7" fill="none" stroke="#ffffff" stroke-width="1.3"/>
          </svg>
          KLXCorvaneElectric@mailvex.net
        </li>
      </ul>
    </div>
    <div class="accent-band"></div>
  </section>

  <section class="card card-back">
    <p class="brand-name">Corvane<br>Electric</p>
  </section>
</main>
</body>
</html>
```